Referral Club PostCard/ Index Card

I need to create an Index card for a Contractor Referral Club. I already did my own door hanger which I can show you. Cost is a factor because I'm just starting my company. You guys have already created my 2 logos when I did a previous logo project so I want to use those logos and colors to create a scheme double sided postcard for my referral club attached to our some examples of other ones I've seen. So, you can 1 of 3 different design/color schemes as a basis:
1) The Black background with Blue Shield
2). The Light Blue background with the white wave (Really like this and the black one)
3). My White background blue/black business card design.
So, 3 different design/color schemes to attack?

You can also look at my website for ideas

http://www.TheLanternPointGuide.example
Updates

I have a picture of the things I want to say on BOTH sides on the Index card/[Post card. Basically, there are two versions that can be created, one with the black background/blue logo motif or one with the white/blue background logo. I bought BOTH designs in my logo contest. Actually 1 is the front of the cards and the other is the back of my card. I'm looking for creativity to get these contractors to join this referral club so I can get more leads.

I have some new logos,, icons and pdfs to submit for consideration

Target Market(s)

Drawing Other Contractors into my Professional Referral Exchange Club

Industry/Entity Type

Public Insurance Adjusting

Font styles to use
Serif
Sans Serif
Other font styles liked:
• Love Zurich font but very few people have it..It is eye drawing!!

Colors
0054AA
0677BA
7BADD7
CADEEF
E8F1F8
0094D4
00A9DD
6FCCEA
C7EBF8
E9F6FB
EE7325
F08F49
F5BC92
FAE3D3
FDF4ED

Requirements
Must have
• My Blue or Black/White color scheme to stay consistent to what Ive already had done
Nice to have
• Something that jumps off to entice them to join that I haven't thought of.

```html
<!DOCTYPE html>
<html lang="en">
<head>
<meta charset="utf-8">
<title>Referral Exchange Club – Postcard</title>
<link rel="stylesheet" href="https://fonts.googleapis.com/css2?family=Arimo:wght@400;700&family=Open+Sans:ital,wght@1,600;1,700&family=Tinos&display=swap">
<style>
:root{
  --navy:#0054AA;
  --blue:#0677BA;
  --sky:#00A9DD;
  --title-blue:#1a8fd3;
  --orange:#EE7325;
  --ink:#1d1d1f;
  --dark:#2a2a2c;
  --stage:#939598;
  --paper:#ffffff;
  --band:#f2f2f2;
  --soft-text:#d9d9d9;
  --muted:#8a8a8a;
  --red:#e02020;
}
*{margin:0;padding:0;box-sizing:border-box}
html,body{width:1033px;height:1200px;overflow:hidden;background:var(--paper)}
.stage{position:absolute;left:58px;top:0;width:951px;height:1170px;background:var(--stage)}
.card{position:absolute;left:235px;width:600px;overflow:hidden;box-shadow:6px 8px 10px rgba(0,0,0,.35)}
.card svg.bg{position:absolute;left:0;top:0;width:100%;height:100%}
.card--front{top:143px;height:401px}
.card--back{top:616px;height:399px}
.abs{position:absolute}
.serif{font-family:"Tinos","Times New Roman",serif;font-weight:400}
.sans{font-family:"Arimo",Arial,sans-serif}

/* front */
.club-title{left:0;width:316px;top:48px;text-align:center;color:var(--title-blue);font-size:32px;line-height:40px;letter-spacing:.5px}
.club-roles{left:0;width:316px;top:150px;text-align:center;font-family:"Open Sans",Arial,sans-serif;font-style:italic;font-weight:600;font-size:11.5px;line-height:16px;color:var(--soft-text)}
.join-label{left:0;width:316px;top:213px;text-align:center;color:var(--orange);font-weight:700;font-size:16.5px}
.join-button{left:22px;top:245px;width:258px;height:28px;border-radius:7px;background:linear-gradient(180deg,#2ea3e0,#0677BA);color:#fff;font-size:12px;line-height:28px;text-align:center}
.best-of{left:0;width:316px;top:297px;text-align:center;color:var(--muted);font-size:13px}
.rating{left:500px;top:11px;width:100px;text-align:center}
.rating-head{color:var(--red);font-weight:700;font-size:14px}
.rating-note{font-family:"Tinos",serif;font-size:6px;line-height:6.5px;color:#333}
.brand{left:345px;top:108px;width:240px;text-align:center}
.brand-mark{width:40px;height:40px;background:var(--navy);margin:0 auto 16px}
.brand-name{font-family:"Arimo",Arial,sans-serif;font-weight:400;color:var(--navy);font-size:20px;line-height:22px;letter-spacing:.3px}
.tagline{left:345px;top:242px;width:240px;text-align:center;font-family:"Open Sans",Arial,sans-serif;font-style:italic;font-weight:700;color:var(--blue);font-size:10.5px;letter-spacing:4px}
.service-area{left:270px;width:330px;top:340px;text-align:center;color:#fff;font-size:12px}
.call{left:270px;width:330px;top:357px;text-align:center;color:#fff;font-size:26px}

/* back */
.reasons-title{left:0;width:600px;top:40px;text-align:center;color:var(--title-blue);font-size:27px;line-height:35px}
.reasons{list-style:none;left:38px;top:120px;width:540px}
.reason{position:relative;height:0}
.reason-num{position:absolute;left:0;width:30px;height:30px;border-radius:50%;border-left:1.5px solid var(--orange);border-bottom:1.5px solid var(--orange);color:#fff;font-family:"Arimo",Arial,sans-serif;font-size:17px;line-height:30px;text-align:center}
.reason-text{position:absolute;left:45px;color:#e6e6e6;font-family:"Arimo",Arial,sans-serif;font-size:16px;line-height:19px;white-space:nowrap}
.store{font-weight:700;color:#9a9a9a;font-size:21px;letter-spacing:.5px}
.review{left:63px;top:352px;color:#000;font-size:18px}
.back-brand-mark{left:490px;top:262px;width:62px;height:62px;border-radius:50%;background:linear-gradient(180deg,#6FCCEA,var(--sky))}
.back-brand-name{left:466px;top:350px;width:110px;text-align:center;font-family:"Arimo",Arial,sans-serif;color:var(--navy);font-size:12px;line-height:14px}
</style>
</head>
<body>
<div class="stage"></div>

<section class="card card--front">
  <svg class="bg" viewBox="0 0 600 401" preserveAspectRatio="none">
    <defs>
      <radialGradient id="frontTexture" cx="35%" cy="45%" r="70%">
        <stop offset="0" stop-color="#5a5a5c"/>
        <stop offset="1" stop-color="#1e1e20"/>
      </radialGradient>
      <linearGradient id="frontWave" x1="0" x2="1" y1="0" y2="0">
        <stop offset="0" stop-color="#00A9DD"/>
        <stop offset="1" stop-color="#0054AA"/>
      </linearGradient>
    </defs>
    <rect width="600" height="401" fill="url(#frontTexture)" role="img" aria-label="Dark textured storm-damage photo background"/>
    <path d="M355 0H600V401H200C275 320 340 190 355 0Z" fill="#fff"/>
    <path d="M195 401C300 310 450 278 600 288V401Z" fill="#2a2a2c"/>
    <path d="M222 401C330 332 470 305 600 302V401Z" fill="url(#frontWave)"/>
  </svg>
  <h1 class="abs serif club-title">REFERAL<br>EXCHANGE CLUB</h1>
  <p class="abs club-roles">Public Adjusters &amp; Loss Consultants<br>Damage Assessors &amp; Certified Insurance Appraisers</p>
  <p class="abs sans join-label">TO JOIN CLUB CLICK:</p>
  <div class="abs sans join-button">connectly&nbsp; I Marcus Hale I Exchange Club</div>
  <p class="abs sans best-of">Best of the South 8x since 2010</p>
  <div class="abs rating">
    <p class="sans rating-head">A+ Rating</p>
    <p class="rating-note">Highest Rating For<br>Public Insurance Adjusters<br>(Source: Consumer Reviews)</p>
  </div>
  <div class="abs brand">
    <div class="brand-mark"></div>
    <p class="brand-name">THE LANTERN<br>POINT GUIDE</p>
  </div>
  <p class="abs tagline">FOR THE POLICYHOLDER</p>
  <p class="abs sans service-area">Servicing Florida, Georgia, Alabama and Mississippi</p>
  <p class="abs serif call">CALL 1-800-555-0142</p>
</section>

<section class="card card--back">
  <svg class="bg" viewBox="0 0 600 399" preserveAspectRatio="none">
    <defs>
      <radialGradient id="backTexture" cx="50%" cy="30%" r="70%">
        <stop offset="0" stop-color="#5c5c5e"/>
        <stop offset="1" stop-color="#1c1c1e"/>
      </radialGradient>
      <linearGradient id="backWave" x1="0" x2="1">
        <stop offset="0" stop-color="#00A9DD"/>
        <stop offset="1" stop-color="#0054AA"/>
      </linearGradient>
    </defs>
    <rect width="600" height="399" fill="url(#backTexture)" role="img" aria-label="Dark textured house photo background"/>
    <path d="M0 336C180 296 420 296 600 330V399H0Z" fill="url(#backWave)"/>
    <path d="M0 342C180 304 420 304 600 338V399H0Z" fill="#f2f2f2"/>
  </svg>
  <h2 class="abs serif reasons-title">TOP FOUR REASONS<br>FOR JOINING THE CLUB</h2>
  <ol class="abs reasons">
    <li class="reason"><span class="reason-num" style="top:0">1</span><span class="reason-text" style="top:5px">EXCLUSIVITY ONLY ONE PER INDUSTRY PER REGION</span></li>
    <li class="reason"><span class="reason-num" style="top:47px">2</span><span class="reason-text" style="top:52px">GUARANTEED RETURN REFERRAL “ACCOUNTABILITY”</span></li>
    <li class="reason"><span class="reason-num" style="top:88px">3</span><span class="reason-text" style="top:90px">$75 GIFT CERTIFICATE &nbsp;<span class="store">Harborfresh</span>&nbsp; OR &nbsp;<span class="store">Grovemart</span></span></li>
    <li class="reason"><span class="reason-num" style="top:137px">4</span><span class="reason-text" style="top:132px">TRUST YOUR CLIENT HAS THE BEST LOCAL<br>PUBLIC ADMINISTER</span></li>
  </ol>
  <p class="abs sans review">COMPLIMENTARY POLICY &amp; CLAIM REVIEW</p>
  <div class="abs back-brand-mark"></div>
  <p class="abs back-brand-name">LANTERN POINT</p>
</section>
</body>
</html>
```